QR TILL WORKS , CREDIT CARD PROCESSING EQUIPMENT

qrtillworks is a sub division of Tallow a credit car processing co.
dale ostrander
14 cedar hollow ln
brennard falls qx 07312
suite 412

qrtillworks.example
cell 555-214-7730
office 555-861-2093
we sell pos systems to merchant who want to accept credit cards at there retail location.
black card would be nice buit open to different ideas

Target Market(s)

retail merchants

Industry/Entity Type

credit card processing

Contact Information for Business Card

card should include web site phone address

Colors

Designer to choose colors to be used in the design.

Requirements
Should not have
• red

```html
<!DOCTYPE html>
<html lang="en">
<head>
<meta charset="utf-8">
<title>QR Till Works — Business Card</title>
<link href="https://fonts.googleapis.com/css2?family=Montserrat:wght@400;500;700&display=swap" rel="stylesheet">
<style>
  :root {
    --backdrop: #2b2b2b;
    --card-black: #141414;
    --card-white: #f7f7f7;
    --accent-yellow: #f0bb22;
    --ink: #111111;
    --paper-text: #ffffff;
  }
  * { margin: 0; padding: 0; box-sizing: border-box; }
  html, body {
    width: 1200px;
    height: 797px;
    overflow: hidden;
    background: var(--backdrop);
    font-family: "Montserrat", sans-serif;
  }
  .canvas {
    position: relative;
    width: 1200px;
    height: 797px;
    display: flex;
    align-items: center;
    justify-content: center;
    gap: 60px;
  }
  .card {
    position: relative;
    width: 520px;
    height: 297px;
    overflow: hidden;
    box-shadow: 0 18px 40px rgba(0,0,0,0.45);
  }

  /* Front */
  .card-front {
    background: var(--card-black);
    color: var(--paper-text);
  }
  .brand {
    position: absolute;
    top: 98px;
    left: 0;
    right: 0;
    display: flex;
    align-items: center;
    justify-content: center;
    gap: 14px;
  }
  .brand-dot {
    width: 18px;
    height: 18px;
    border-radius: 50%;
    background: var(--accent-yellow);
  }
  .brand-name {
    font-weight: 500;
    font-size: 40px;
    letter-spacing: 1px;
    color: var(--paper-text);
  }
  .front-web {
    position: absolute;
    bottom: 44px;
    left: 0;
    right: 0;
    text-align: center;
    font-weight: 500;
    font-size: 13px;
    letter-spacing: 4px;
  }

  /* Back */
  .card-back {
    background: var(--card-white);
    color: var(--ink);
  }
  .band {
    position: absolute;
    left: 0;
    bottom: 0;
    width: 520px;
    height: 100px;
  }
  .band polygon { fill: var(--accent-yellow); }
  .back-web {
    position: absolute;
    left: 0;
    width: 380px;
    bottom: 40px;
    text-align: center;
    font-weight: 700;
    font-size: 13px;
    letter-spacing: 3px;
  }
  .details {
    position: absolute;
    top: 54px;
    left: 32px;
    display: flex;
    align-items: stretch;
  }
  .address {
    text-align: right;
    padding-right: 14px;
    border-right: 2px solid var(--ink);
    font-size: 14px;
    line-height: 1.35;
  }
  .person-name {
    font-weight: 700;
    font-size: 19px;
    letter-spacing: 0.3px;
    text-transform: uppercase;
    margin-bottom: 2px;
  }
  .phones {
    padding-left: 14px;
    padding-top: 46px;
    font-size: 14px;
    line-height: 1.4;
  }
  .phone-row { display: flex; gap: 8px; }
  .phone-label { font-weight: 700; width: 52px; }
</style>
</head>
<body>
<main class="canvas">
  <section class="card card-front" aria-label="Business card front">
    <div class="brand">
      <span class="brand-dot"></span>
      <span class="brand-name">QR TILL WORKS</span>
    </div>
    <p class="front-web">qrtillworks.example</p>
  </section>

  <section class="card card-back" aria-label="Business card back">
    <div class="details">
      <div class="address">
        <p class="person-name">Dale Ostrander</p>
        <p>14 cedar hollow ln</p>
        <p>brennard falls qx 07312</p>
        <p>suite 412</p>
      </div>
      <div class="phones">
        <p class="phone-row"><span class="phone-label">Cell:</span><span>555-214-7730</span></p>
        <p class="phone-row"><span class="phone-label">Office:</span><span>555-861-2093</span></p>
      </div>
    </div>
    <svg class="band" viewBox="0 0 520 100" aria-hidden="true">
      <polygon points="0,10 178,30 186,16 192,32 520,68 520,100 0,100"/>
    </svg>
    <p class="back-web">qrtillworks.example</p>
  </section>
</main>
</body>
</html>
```